Trifold flyer for our dental clinic (the Bright Harbor Clinic)

The goal of this project is to design a trifold flyer for our dental clinic (the Bright Harbor Clinic). The winning design is expected to be creative, artistic and coherent with our logo.
Updates

Designs look the same

Target Market(s)

Young generation with dental need.

Industry/Entity Type

Dental Clinic

Font styles to use
Sans Serif

Colors
0355a3
85acd3
85cae6
0592cd
00a990
86cfc6
cedeed
cee9f5
cfeae6

Requirements
Must have
• See the attached sketch for content arrangement.

```html
<!DOCTYPE html>
<html lang="en">
<head>
<meta charset="utf-8">
<title>Bright Harbor Clinic – Trifold Outside</title>
<link rel="stylesheet" href="https://fonts.googleapis.com/css2?family=Montserrat:wght@400;600;700;800&family=Open+Sans:wght@400;600;700&display=swap">
<style>
  :root{
    --navy:#0355a3;
    --blue:#0592cd;
    --sky:#85cae6;
    --soft:#cee9f5;
    --mist:#cedeed;
    --teal:#00a990;
    --yellow:#ffd21f;
    --ink:#4a5560;
    --white:#ffffff;
    --stage:#eceef1;
  }
  *{box-sizing:border-box;margin:0;padding:0}
  html,body{width:831px;height:1200px;overflow:hidden}
  body{background:var(--stage);font-family:"Open Sans",Arial,sans-serif;color:var(--ink);position:relative}
  .brochure{position:absolute;left:10px;top:340px;width:811px;height:520px;display:flex;background:var(--white);box-shadow:0 4px 18px rgba(0,0,0,.15)}
  .panel{position:relative;width:33.333%;height:100%;overflow:hidden}
  .panel + .panel{border-left:1px solid #e3e8ee}

  /* Meet us */
  .meet{padding:22px 20px 0 20px;background:linear-gradient(180deg,var(--white) 0%,#f1f6fb 100%)}
  .heading{font-family:"Montserrat",Arial,sans-serif;font-weight:800;font-size:21px;color:var(--navy);letter-spacing:.5px}
  .doctor{margin-top:18px}
  .doctor-head{display:flex;align-items:center;gap:10px}
  .portrait{flex:0 0 50px;width:50px;height:50px;border-radius:50%;border:3px solid var(--soft);background:radial-gradient(circle at 50% 40%,#d9c2ae,#8d9aa6)}
  .doctor-name{font-family:"Montserrat",Arial,sans-serif;font-weight:700;font-size:10.5px;color:var(--navy)}
  .doctor-title{font-size:7.5px;color:var(--blue);margin-top:2px}
  .doctor-bio{font-size:7.5px;line-height:1.5;margin-top:8px}

  /* Reviews / contact */
  .reviews-band{position:absolute;left:0;top:0;width:100%;height:300px}
  .reviews-text{position:absolute;left:20px;right:20px;top:18px;color:var(--white)}
  .reviews-text .heading{color:var(--white)}
  .review{font-size:7.5px;line-height:1.5;margin-top:10px}
  .review-by{text-align:right;font-weight:700;font-size:7px;margin-top:3px;color:var(--sky)}
  .hero-circle{position:absolute;left:50%;top:178px;width:180px;height:180px;margin-left:-90px;border-radius:50%;border:6px solid var(--white);background:radial-gradient(circle at 45% 40%,#e7c9a6 0,#a8b86a 55%,#5f8f3c 100%);box-shadow:0 2px 8px rgba(0,0,0,.15)}
  .contact{position:absolute;left:0;right:0;top:370px;text-align:center}
  .contact .heading{font-size:19px}
  .contact-sub{font-size:8px;margin-top:2px}
  .contact-icons{display:flex;justify-content:center;gap:7px;margin-top:10px}
  .contact-icons span{width:20px;height:20px;border-radius:50%;background:var(--navy);display:block}
  .contact-lines{margin-top:10px;font-size:9px;line-height:1.6;color:var(--navy);font-weight:600}

  /* Offers */
  .brand{position:absolute;left:0;right:0;top:18px;display:flex;justify-content:center;align-items:center;gap:8px}
  .brand-square{width:22px;height:22px;background:var(--blue)}
  .brand-name{font-family:"Montserrat",Arial,sans-serif;font-weight:700;font-size:14px;color:var(--navy);line-height:1.1}
  .family-photo{position:absolute;left:0;top:62px;width:100%;height:250px;background:linear-gradient(160deg,#c8dfa0 0%,#8fbf55 45%,#b5533a 80%,#7a3d2a 100%)}
  .offers-band{position:absolute;left:0;top:262px;width:100%;height:258px}
  .offers-text{position:absolute;left:18px;right:18px;top:322px;color:var(--white)}
  .offers-title{font-family:"Montserrat",Arial,sans-serif;font-weight:800;font-size:36px;line-height:.95;color:var(--yellow);text-align:right}
  .offers-grid{display:flex;justify-content:space-between;margin-top:22px;text-align:center}
  .offers-grid > div{flex:1}
  .offer-price{font-family:"Montserrat",Arial,sans-serif;font-weight:800;font-size:19px;color:var(--yellow);white-space:nowrap}
  .offer-label{font-size:8px;line-height:1.35;margin-top:4px}
</style>
</head>
<body>
<main class="brochure">

  <section class="panel meet">
    <h2 class="heading">MEET US</h2>
    <article class="doctor">
      <div class="doctor-head">
        <div class="portrait" role="img" aria-label="Portrait photo of Dr. Elena Reyes"></div>
        <div><p class="doctor-name">ELENA REYES, DMD, MS</p><p class="doctor-title">Board Certified Orthodontist</p></div>
      </div>
      <p class="doctor-bio">Dr. Reyes earned her dental degree with honors and has guided thousands of patients toward healthy, confident smiles with gentle, modern orthodontic care.</p>
    </article>
    <article class="doctor">
      <div class="doctor-head">
        <div class="portrait" role="img" aria-label="Portrait photo of Dr. Thomas R. Lowell"></div>
        <div><p class="doctor-name">THOMAS R. LOWELL, DMD, MS</p><p class="doctor-title">Board Certified Orthodontist</p></div>
      </div>
      <p class="doctor-bio">Dr. Lowell is a board certified specialist who believes every visit should feel calm, clear and friendly, from first exam to final check.</p>
    </article>
    <article class="doctor">
      <div class="doctor-head">
        <div class="portrait" role="img" aria-label="Portrait photo of Dr. Daniel Navarro"></div>
        <div><p class="doctor-name">DANIEL NAVARRO, DMD</p><p class="doctor-title">General Dentist</p></div>
      </div>
      <p class="doctor-bio">Dr. Navarro brings years of family dentistry experience and a warm approach that helps children and adults feel at ease in the chair.</p>
    </article>
  </section>

  <section class="panel">
    <svg class="reviews-band" viewBox="0 0 270 300" preserveAspectRatio="none" aria-hidden="true">
      <path d="M0 0H270V230Q135 300 0 230Z" fill="var(--navy)"/>
    </svg>
    <div class="reviews-text">
      <h2 class="heading">REVIEWS</h2>
      <p class="review">The whole team made me feel welcome from the moment I walked in. My treatment was explained clearly, the staff was patient with every question, and my new smile looks amazing. I recommend them to everyone.</p>
      <p class="review-by">— Angela M., patient</p>
      <p class="review">Booking was easy, the office is spotless and the doctors are truly kind. My kids actually look forward to their checkups now.</p>
      <p class="review-by">— Marcus T., parent</p>
    </div>
    <div class="hero-circle" role="img" aria-label="Photo of a smiling young woman outdoors"></div>
    <div class="contact">
      <h2 class="heading">CONTACT US</h2>
      <p class="contact-sub">To find out more please</p>
      <div class="contact-icons"><span></span><span></span><span></span><span></span></div>
      <p class="contact-lines">1-555-014-2380<br>www.brightharborclinic.com<br>info@brightharborclinic.com</p>
    </div>
  </section>

  <section class="panel">
    <div class="brand"><span class="brand-square"></span><span class="brand-name">BRIGHT HARBOR<br>CLINIC</span></div>
    <div class="family-photo" role="img" aria-label="Photo of a smiling family holding a basket of apples in a green field"></div>
    <svg class="offers-band" viewBox="0 0 270 258" preserveAspectRatio="none" aria-hidden="true">
      <path d="M0 40Q135 -20 270 40V258H0Z" fill="var(--navy)"/>
      <path d="M0 40Q135 -20 270 40" fill="none" stroke="var(--sky)" stroke-width="4"/>
    </svg>
    <div class="offers-text">
      <h2 class="offers-title">SPECIAL<br>OFFERS</h2>
      <div class="offers-grid">
        <div><p class="offer-price">$69</p><p class="offer-label">New Patients<br>Special</p></div>
        <div><p class="offer-price">$69</p><p class="offer-label">In Office Teeth<br>Whitening</p></div>
        <div><p class="offer-price">25%-40%</p><p class="offer-label">Off On<br>Clear Aligners</p></div>
      </div>
    </div>
  </section>

</main>
</body>
</html>
```